BrennoraVault.com -Ecommerce Website for Luxury Products

This will be an ecommerce site. A website portal that will allow both consumers to enter one way and see specific purchase options and businesses to enter via a different link that allows B2B to see their specific options once logged into. B2C can purchase both as a guest/or after account is setup. B2B must be approved to set up account. This is front end website project. Back-end integration is separate. Will be hosted on Servaplex with a domain registration held at NimbraGate. Additional website concept/idea/synergy can be found from sister site-KWRMHospitality.com

```html
<!DOCTYPE html>
<html lang="en">
<head>
<meta charset="utf-8">
<title>BrennoraVault – Purveyors of Luxury Lifestyle Accoutrements</title>
<link href="https://fonts.googleapis.com/css2?family=Merriweather:wght@700;900&family=Lato:ital,wght@0,400;0,700;1,400&display=swap" rel="stylesheet">
<style>
:root{
  --gold:#c6a15b;
  --ink:#1c1c1c;
  --body:#444;
  --cream:#fcf8f4;
  --white:#fff;
  --dark:#1a1612;
  --footer:#1f1b17;
  --line:#e4ddd2;
}
*{box-sizing:border-box;margin:0;padding:0}
html,body{width:1200px;height:3094px;overflow:hidden}
body{font-family:"Lato",sans-serif;color:var(--ink);background:var(--white);position:relative}
a{color:inherit;text-decoration:none}

/* header */
.site-header{height:88px;border-top:3px solid var(--gold);display:flex;align-items:center;padding:0 110px;position:relative;background:var(--white)}
.brand{display:flex;flex-direction:column;align-items:center;width:150px;white-space:nowrap}
.brand-mark{width:18px;height:18px;border:1.5px solid var(--ink);margin-bottom:4px}
.brand-name{font-family:"Merriweather",serif;font-size:15px;font-weight:700;letter-spacing:.5px}
.brand-div{font-size:5px;letter-spacing:1px;font-weight:700}
.brand-tag{font-family:"Merriweather",serif;font-size:6px}
.main-nav{display:flex;gap:27px;margin-left:108px;font-size:15px}
.main-nav a.active{color:var(--gold);text-decoration:underline}
.header-icons{display:flex;gap:12px;margin-left:25px;align-items:center}
.btn-gold{background:var(--gold);color:var(--white);font-weight:700;border-radius:4px;display:inline-flex;align-items:center;justify-content:center}
.header-cta{margin-left:auto;width:131px;height:47px;font-size:17px}

/* hero */
.hero{height:596px;background:linear-gradient(100deg,#3a1f10 0%,#6b3a1a 40%,#9a5a25 70%,#5a2e12 100%);position:relative}
.hero-content{position:absolute;left:110px;top:196px}
.hero h1{font-family:"Merriweather",serif;font-weight:900;font-size:50px;line-height:64px;color:var(--white);width:760px}
.hero .btn-gold{margin-top:28px;width:215px;height:47px;font-size:17px}

/* about */
.about{height:576px;position:relative}
.about-frame{position:absolute;left:110px;top:81px;width:414px;height:381px;border:3px solid var(--ink);border-radius:6px}
.about-photo{position:absolute;left:124px;top:96px;width:432px;height:396px;background:linear-gradient(160deg,#5a3a1e,#b07a3e 55%,#d8a766);border-radius:4px;box-shadow:0 4px 12px rgba(0,0,0,.15)}
.about-text{position:absolute;left:640px;top:72px;width:448px}
.about-text h2{font-family:"Merriweather",serif;font-size:36px;font-weight:700}
.rule{width:90px;height:3px;background:var(--gold)}
.about-text .rule{margin:22px 0 20px}
.about-text p{font-size:15px;line-height:26px;color:var(--body);text-align:justify;margin-bottom:15px}
.about-text .btn-gold{width:130px;height:47px;font-size:17px;margin-top:8px}

/* featured */
.featured{height:628px;background:var(--cream);position:relative}
.section-title{text-align:center;font-family:"Merriweather",serif;font-size:36px;font-weight:700;padding-top:74px}
.section-title + .rule{margin:14px auto 0}
.arrow{position:absolute;width:32px;height:32px;border:1.5px solid var(--ink);border-radius:50%;display:flex;align-items:center;justify-content:center;background:var(--white)}
.collection-grid{position:absolute;left:110px;top:170px;display:flex;gap:29px}
.collection-card{width:307px;height:375px;background:var(--white);border:1px solid var(--line);border-radius:4px;box-shadow:0 2px 6px rgba(0,0,0,.08);overflow:hidden}
.collection-card .media{height:220px}
.collection-card .body{padding:20px 27px}
.collection-card h3{font-family:"Merriweather",serif;font-size:23px;font-weight:700;margin-bottom:12px}
.collection-card p{font-size:15px;line-height:26px;color:var(--body)}
.collection-card .more{font-size:14px;font-style:italic;text-decoration:underline;display:block;margin-top:4px}

/* cta */
.cta{height:362px;background:radial-gradient(ellipse at 30% 40%,#3a2e28,#141110 75%);text-align:center;color:var(--white)}
.cta h2{font-family:"Merriweather",serif;font-size:37px;font-weight:700;padding-top:72px}
.cta p{font-size:15px;line-height:26px;width:760px;margin:26px auto 0}
.btn-white{display:inline-flex;align-items:center;justify-content:center;background:var(--white);color:var(--ink);width:214px;height:47px;font-size:17px;border-radius:3px;margin-top:28px}

/* partners */
.partners{height:492px;position:relative}
.partners .section-title{padding-top:68px}
.partner-grid{position:absolute;left:111px;top:160px;display:flex;gap:16px}
.partner-card{width:232px;height:246px;background:var(--white);border:1px solid var(--line);border-radius:4px;box-shadow:0 2px 6px rgba(0,0,0,.1);overflow:hidden}
.partner-card .media{height:174px}
.partner-card .info{display:flex;justify-content:space-between;align-items:center;padding:14px 18px 0}
.partner-card h4{font-family:"Merriweather",serif;font-size:18px;font-weight:700;line-height:26px;white-space:nowrap}
.badge{width:50px;height:50px;border-radius:50%;background:#e9e2d6;flex:none}

/* footer */
.site-footer{height:354px;background:radial-gradient(ellipse at 70% 40%,#2c251f,var(--footer) 70%);color:var(--white);position:relative}
.footer-brand{position:absolute;left:110px;top:80px;width:250px;display:flex;flex-direction:column;align-items:center;white-space:nowrap}
.footer-brand .brand-mark{border-color:var(--white);width:28px;height:28px}
.footer-brand .brand-name{font-size:25px}
.footer-brand .brand-div{font-size:9px;letter-spacing:2px}
.footer-brand .brand-tag{font-size:11px;margin-top:6px}
.footer-col{position:absolute;top:88px}
.footer-col h5{font-size:17px;font-weight:400;margin-bottom:12px}
.footer-col ul{list-style:none}
.footer-col li{font-size:15px;line-height:34px;padding-left:24px;position:relative}
.footer-col li::before{content:"";position:absolute;left:3px;top:14px;width:7px;height:7px;border-radius:50%;background:var(--white)}
.contact-row{display:flex;gap:10px;font-size:15px;line-height:26px;margin-bottom:20px}
.contact-row svg{flex:none;margin-top:5px}
.footer-bottom{position:absolute;left:110px;right:110px;top:297px;border-top:1px solid #4a423a;padding-top:18px;display:flex;justify-content:space-between;align-items:center;font-size:15px}
.socials{display:flex;gap:10px}
.socials span{width:22px;height:22px;border-radius:50%;background:var(--white)}
</style>
</head>
<body>

<header class="site-header">
  <div class="brand">
    <span class="brand-mark"></span>
    <span class="brand-name">BRENNORAVAULT</span>
    <span class="brand-div">A DIVISION OF KWRM HOSPITALITY</span>
    <span class="brand-tag">Purveyors of Luxury Lifestyle Accoutrements</span>
  </div>
  <nav class="main-nav">
    <a class="active" href="#">Home</a>
    <a href="#">About Us</a>
    <a href="#">Retail Collections</a>
    <a href="#">Wholesale Portal</a>
    <a href="#">Partner</a>
  </nav>
  <div class="header-icons">
    <svg width="22" height="22" viewBox="0 0 22 22"><circle cx="9" cy="9" r="7" fill="none" stroke="#1c1c1c" stroke-width="2"/><line x1="14" y1="14" x2="20" y2="20" stroke="#1c1c1c" stroke-width="2.4"/></svg>
    <svg width="22" height="22" viewBox="0 0 22 22"><path d="M1 3h4l3 11h10l3-8H7" fill="#1c1c1c" stroke="#1c1c1c" stroke-width="1.5"/><circle cx="9" cy="18" r="2" fill="#1c1c1c"/><circle cx="17" cy="18" r="2" fill="#1c1c1c"/></svg>
  </div>
  <a class="btn-gold header-cta" href="#">Contact Us</a>
</header>

<section class="hero" role="img" aria-label="Warm-lit luxury lounge bar with wood panelling, backlit bottle shelves and leather chairs">
  <div class="hero-content">
    <h1>Purveyors of Luxury Lifestyle Accoutrements</h1>
    <a class="btn-gold" href="#">Explore the Collection</a>
  </div>
</section>

<section class="about">
  <div class="about-frame"></div>
  <div class="about-photo" role="img" aria-label="Elegant dining table set with glassware, napkins and pine cone centrepiece"></div>
  <div class="about-text">
    <h2>About BrennoraVault</h2>
    <div class="rule"></div>
    <p>BrennoraVault is a curated luxury destination created for those who value distinction, craftsmanship, and refined indulgence. We specialize in sourcing and developing elevated lifestyle accoutrements—designed to be experienced personally and showcased professionally.</p>
    <p>As a division of KWRM Hospitality, BrennoraVault brings a hospitality-first mindset into the world of luxury retail and wholesale. We understand not only what defines exceptional products, but how they enhance atmosphere, presence, and perception.</p>
    <a class="btn-gold" href="#">Read More</a>
  </div>
</section>

<section class="featured">
  <h2 class="section-title">Featured Collections</h2>
  <div class="rule"></div>
  <span class="arrow" style="left:35px;top:342px"><svg width="12" height="12" viewBox="0 0 12 12"><path d="M8 1 3 6l5 5" fill="none" stroke="#1c1c1c" stroke-width="1.4"/></svg></span>
  <span class="arrow" style="left:1133px;top:342px"><svg width="12" height="12" viewBox="0 0 12 12"><path d="M4 1l5 5-5 5" fill="none" stroke="#1c1c1c" stroke-width="1.4"/></svg></span>
  <div class="collection-grid">
    <article class="collection-card">
      <div class="media" role="img" aria-label="Wooden humidor shelves stocked with cigars" style="background:linear-gradient(150deg,#3b1f0e,#8a5428 60%,#b57a3f)"></div>
      <div class="body">
        <h3>Cigar Accessories</h3>
        <p>Elevated accessories designed to complement the ritual. Crafted for</p>
        <a class="more" href="#">Read More</a>
      </div>
    </article>
    <article class="collection-card">
      <div class="media" role="img" aria-label="Cigars on a leather tray beside a glass of spirits" style="background:linear-gradient(150deg,#2a170b,#6e3e1b 55%,#a46a35)"></div>
      <div class="body">
        <h3>Attire and Accessories</h3>
        <p>Sophisticated fragrance profiles and oils created to leave a lasting</p>
        <a class="more" href="#">Read More</a>
      </div>
    </article>
    <article class="collection-card">
      <div class="media" role="img" aria-label="Shopper testing perfume in a bright fragrance boutique" style="background:linear-gradient(150deg,#eadfd8,#d9b9a6 55%,#b7826c)"></div>
      <div class="body">
        <h3>Fragrances</h3>
        <p>Elevated accessories designed to complement the ritual. Crafted for</p>
        <a class="more" href="#">Read More</a>
      </div>
    </article>
  </div>
</section>

<section class="cta">
  <h2>Elevate Your Lounge Impress Your Clientele</h2>
  <p>BrennoraVault partners with premium lounges, hospitality venues, and licensed operators to provide exclusive lifestyle products that enhance atmosphere and brand perception.</p>
  <a class="btn-white" href="#">Shop BrennoraVault</a>
</section>

<section class="partners">
  <h2 class="section-title">Our Partners</h2>
  <div class="rule"></div>
  <span class="arrow" style="left:35px;top:268px"><svg width="12" height="12" viewBox="0 0 12 12"><path d="M8 1 3 6l5 5" fill="none" stroke="#1c1c1c" stroke-width="1.4"/></svg></span>
  <span class="arrow" style="left:1133px;top:268px"><svg width="12" height="12" viewBox="0 0 12 12"><path d="M4 1l5 5-5 5" fill="none" stroke="#1c1c1c" stroke-width="1.4"/></svg></span>
  <div class="partner-grid">
    <article class="partner-card">
      <div class="media" role="img" aria-label="Crystal decanter and whisky glasses on a dark bar" style="background:linear-gradient(160deg,#2b241f,#6a5442 60%,#a88a6a)"></div>
      <div class="info"><h4>The Onyx<br>Parlour</h4><span class="badge"></span></div>
    </article>
    <article class="partner-card">
      <div class="media" role="img" aria-label="Cocktail glass with cigar smoke in a lounge" style="background:linear-gradient(160deg,#3a3532,#8a7a68 55%,#c9b497)"></div>
      <div class="info"><h4>Amber Coal<br>Lounge</h4><span class="badge"></span></div>
    </article>
    <article class="partner-card">
      <div class="media" role="img" aria-label="Whisky glass and smoking cigar on a red-lit table" style="background:linear-gradient(160deg,#1d0f09,#5e2412 55%,#a4502a)"></div>
      <div class="info"><h4>The Cedar<br>Humidor</h4><span class="badge"></span></div>
    </article>
    <article class="partner-card">
      <div class="media" role="img" aria-label="Cigar resting in an ashtray beside red leather seating" style="background:linear-gradient(160deg,#2a120b,#7a2a1a 55%,#b8743c)"></div>
      <div class="info"><h4>The Meridian<br>Cigar Salon</h4><span class="badge"></span></div>
    </article>
  </div>
</section>

<footer class="site-footer">
  <div class="footer-brand">
    <span class="brand-mark"></span>
    <span class="brand-name">BRENNORAVAULT</span>
    <span class="brand-div">A DIVISION OF KWRM HOSPITALITY</span>
    <span class="brand-tag">Purveyors of Luxury Lifestyle Accoutrements</span>
  </div>
  <div class="footer-col" style="left:426px">
    <h5>Quick Links</h5>
    <ul><li>Home</li><li>About Us</li><li>Retail Collections</li><li>Wholesale Portal</li><li>Partner</li></ul>
  </div>
  <div class="footer-col" style="left:628px">
    <h5>Support &amp; Policies</h5>
    <ul><li>Retail Collections</li><li>Cigar &amp; Lounge Essentials</li><li>Fragrances &amp; Signature Oils</li><li>Apparel &amp; Accessories</li></ul>
  </div>
  <div class="footer-col" style="left:886px;width:210px">
    <h5>Contact Us</h5>
    <div class="contact-row"><svg width="16" height="18" viewBox="0 0 16 18"><path d="M8 1a6 6 0 0 0-6 6c0 4.5 6 10 6 10s6-5.5 6-10a6 6 0 0 0-6-6z" fill="#fff"/><circle cx="8" cy="7" r="2.3" fill="#1f1b17"/></svg><span>Harrow Street. 82 Linden Ave, Marlow City, 20418,</span></div>
    <div class="contact-row"><svg width="16" height="16" viewBox="0 0 16 16"><circle cx="8" cy="8" r="8" fill="#fff"/><rect x="4" y="5" width="8" height="6" fill="none" stroke="#1f1b17" stroke-width="1.2"/><path d="M4 5l4 3 4-3" fill="none" stroke="#1f1b17" stroke-width="1.2"/></svg><span>info@brennoravault.com</span></div>
    <div class="contact-row"><svg width="16" height="16" viewBox="0 0 16 16"><circle cx="8" cy="8" r="8" fill="#fff"/><path d="M5 4l2 2-1 1.3c.6 1.3 1.4 2.1 2.7 2.7L10 9l2 2-1.3 1.3C7.5 12 4 8.5 3.7 5.3z" fill="#1f1b17"/></svg><span>+1 555 014 2290</span></div>
  </div>
  <div class="footer-bottom">
    <div class="socials"><span></span><span></span><span></span><span></span></div>
    <span>© 2026 BrennoraVault. All Rights Reserved.</span>
  </div>
</footer>

</body>
</html>
```